Sell the dream! Property investment proposal document

We are looking for a proposal document which outlines our vision for property development. The purpose of the document is to raise investment from investors - sell the dream!
Brief summary:
Tarrow Dwellings Developments, is an emerging New Zealand property investment company with a focus on providing unique property investment opportunities.
Our expertise and capabilities in architectural modular homes provide us with a remarkable advantage in tackling the development of properties that are typically considered challenging, remote, or uniquely positioned.
Our specialization in this niche sector of property development not only sets us apart from competitors, but also paves the way for lucrative investment opportunities in the New Zealand property market.
Feel free to use any images from www.tarrowdwellings.co.nz
Target Market(s)
investors for a unique property development opportunity
Industry/Entity Type
luxury property development in unique locations throughout New Zealand
Font styles to use
Colors
Designer to choose only greyscale colors for use in the design.
Look and feel

```html
<!DOCTYPE html>
<html lang="en">
<head>
<meta charset="utf-8">
<title>Tarrow Dwellings Developments – Investment Proposal</title>
<link href="https://fonts.googleapis.com/css2?family=Montserrat:wght@300;400;600;700&family=Open+Sans:wght@400;600&display=swap" rel="stylesheet">
<style>
:root{
  --ink:#0b0b0b;
  --charcoal:#1c1c1c;
  --steel:#5a5a5a;
  --mist:#9a9a9a;
  --fog:#d9d9d9;
  --paper:#ffffff;
  --canvas:#ececec;
}
*{margin:0;padding:0;box-sizing:border-box}
html,body{width:857px;height:1200px;overflow:hidden;background:var(--canvas)}
body{position:relative;font-family:'Open Sans',sans-serif}
.page{position:absolute;width:400px;height:583px;overflow:hidden;box-shadow:0 2px 6px rgba(0,0,0,.25)}
.page--cover{left:20px;top:14px;background:var(--ink)}
.page--overview{left:437px;top:8px;background:var(--ink)}
.page--advantage{left:20px;top:606px;background:var(--paper)}
.page--back{left:437px;top:606px;background:var(--paper)}
.photo{position:absolute;left:0;width:100%;background:linear-gradient(180deg,#6f6f6f 0%,#3d3d3d 55%,#1e1e1e 100%)}
.shapes{position:absolute;left:0;width:100%}
.footer{position:absolute;left:22px;bottom:16px;display:flex;align-items:center;gap:7px;font-size:8px;color:var(--fog);font-family:'Montserrat',sans-serif}
.footer svg{width:11px;height:11px}
.footer--dark{color:var(--charcoal)}
.cover-title{position:absolute;left:30px;top:380px;font-family:'Montserrat',sans-serif;font-weight:300;font-size:72px;color:var(--paper);letter-spacing:1px;line-height:1}
.cover-sub{position:absolute;left:32px;top:462px;font-family:'Montserrat',sans-serif;font-size:15px;color:var(--mist);font-weight:400}
.copy{position:absolute;left:30px;right:26px}
h2{font-family:'Montserrat',sans-serif;font-weight:600;font-size:14px;margin-bottom:8px}
.copy p{font-size:5.6px;line-height:1.65;margin-bottom:6px}
.copy--dark h2{color:var(--paper)}
.copy--dark p{color:var(--mist)}
.copy--light h2{color:var(--ink)}
.copy--light p{color:var(--steel)}
.monogram{position:absolute;left:24px;top:445px;font-family:'Montserrat',sans-serif;font-weight:300;font-size:130px;color:var(--paper);line-height:1}
.vertical-name{position:absolute;left:250px;top:70px;writing-mode:vertical-rl;font-family:'Montserrat',sans-serif;font-weight:300;font-size:150px;color:#ebebeb;letter-spacing:4px;line-height:1}
</style>
</head>
<body>

<!-- Cover -->
<section class="page page--cover">
  <div class="photo" style="top:0;height:270px" role="img" aria-label="Photograph of a modern modular home on a coastal hillside at dusk"></div>
  <svg class="shapes" style="top:200px" width="400" height="150" viewBox="0 0 400 150">
    <polygon points="0,70 400,10 400,150 0,150" fill="#0b0b0b"/>
    <polygon points="170,90 400,35 400,60 230,100" fill="#d9d9d9"/>
    <polygon points="0,95 160,150 0,150" fill="#5a5a5a"/>
    <polygon points="300,150 400,95 400,150" fill="#9a9a9a"/>
  </svg>
  <div class="cover-title">Tarrow</div>
  <div class="cover-sub">Modular Architectural Homes</div>
  <div class="footer"><svg viewBox="0 0 12 12"><circle cx="6" cy="6" r="5" fill="none" stroke="#d9d9d9"/><path d="M1 6h10M6 1c2 2 2 8 0 10M6 1c-2 2-2 8 0 10" fill="none" stroke="#d9d9d9" stroke-width=".7"/></svg>www.tarrowdwellings.co.nz</div>
</section>

<!-- Business overview -->
<section class="page page--overview">
  <div class="photo" style="top:0;height:120px" role="img" aria-label="Photograph of a modular home set in open countryside"></div>
  <svg class="shapes" style="top:70px" width="400" height="90" viewBox="0 0 400 90">
    <polygon points="0,60 400,0 400,90 0,90" fill="#0b0b0b"/>
    <polygon points="0,30 120,72 0,90" fill="#d9d9d9"/>
    <polygon points="250,35 400,10 400,30 290,42" fill="#9a9a9a"/>
  </svg>
  <div class="copy copy--dark" style="top:165px">
    <h2>Business Overview</h2>
    <p>Tarrow Dwellings Developments is an emerging New Zealand property investment company with a focus on providing unique property investment opportunities. Our expertise and capabilities in architectural modular homes provide us with a remarkable advantage in tackling the development of properties that are typically considered challenging, remote or uniquely positioned. We see value where others see obstacles, and we build homes that belong to their landscape.</p>
    <p>Our specialisation in this niche sector of property development not only sets us apart from competitors, but also paves the way for lucrative investment opportunities in the New Zealand property market. Each project is planned with care, delivered with precision and designed to hold its value for decades to come.</p>
    <h2 style="margin-top:14px">Business Origins</h2>
    <p>Tarrow Dwellings Developments was founded on a simple belief: remarkable sites deserve remarkable homes. Our founders spent years working across building, design and finance, and saw that many of the most beautiful locations in the country sat untouched because they were too difficult to build on using traditional methods. Modular construction changed that equation.</p>
    <p>By building our homes off site in a controlled environment, we reduce waste, shorten timelines and deliver consistent quality regardless of how remote a site may be. Finished modules are transported and placed with minimal disturbance to the land. This approach allows us to unlock coastal, alpine and rural sites that others pass by, and to offer investors a clear path to returns in a growing segment of the luxury market.</p>
  </div>
  <div class="footer"><svg viewBox="0 0 12 12"><circle cx="6" cy="6" r="5" fill="none" stroke="#d9d9d9"/><path d="M1 6h10M6 1c2 2 2 8 0 10M6 1c-2 2-2 8 0 10" fill="none" stroke="#d9d9d9" stroke-width=".7"/></svg>www.tarrowdwellings.co.nz</div>
</section>

<!-- Competitive advantage -->
<section class="page page--advantage">
  <div class="photo" style="top:0;height:125px" role="img" aria-label="Photograph of a modular home interior opening onto a view"></div>
  <svg class="shapes" style="top:70px" width="400" height="80" viewBox="0 0 400 80">
    <polygon points="0,55 400,5 400,80 0,80" fill="#ffffff"/>
    <polygon points="0,30 150,60 0,70" fill="#1c1c1c"/>
    <polygon points="230,40 400,15 400,35 270,48" fill="#9a9a9a"/>
  </svg>
  <div class="copy copy--light" style="top:160px">
    <h2>Competitive Advantage</h2>
    <p>Our modular approach gives us an edge that few developers can match. We can build on sites with difficult access, steep terrain or limited local trades, while keeping costs predictable and timelines short. Every home is designed by architects and finished to a luxury standard, giving buyers a product that stands out in a crowded market.</p>
    <p>Because construction happens off site, weather delays are minimal and quality control is consistent. This reduces risk for investors and allows capital to be recycled into new projects sooner.</p>
    <h2 style="margin-top:14px">Financial Summary</h2>
    <p>Each development is structured with clear entry and exit points for investors. Projected returns are based on conservative land values, confirmed build costs and realistic sale prices drawn from comparable properties. Funds are held in dedicated project accounts and released against agreed milestones, with regular reporting at every stage.</p>
    <p>We are seeking investment partners to help deliver our next series of developments across unique locations throughout New Zealand, with strong demand expected from local and overseas buyers alike.</p>
  </div>
  <svg class="shapes" style="top:420px" width="400" height="163" viewBox="0 0 400 163">
    <polygon points="0,40 400,0 400,163 0,163" fill="#0b0b0b"/>
    <polygon points="260,30 400,5 400,25 300,38" fill="#d9d9d9"/>
  </svg>
  <div class="monogram">T</div>
  <div class="footer"><svg viewBox="0 0 12 12"><circle cx="6" cy="6" r="5" fill="none" stroke="#d9d9d9"/><path d="M1 6h10M6 1c2 2 2 8 0 10M6 1c-2 2-2 8 0 10" fill="none" stroke="#d9d9d9" stroke-width=".7"/></svg>www.tarrowdwellings.co.nz</div>
</section>

<!-- Back page -->
<section class="page page--back">
  <div class="vertical-name">Tarrow</div>
</section>

</body>
</html>
```